Verdana Glen Website

I need a design of homepage for a health and wellness center. We considers self to be young and fresh and want something along that design. We want a main picture/logo/design (or all three), and underneath that 4 pictures to depict what services we do. The four services are Orthopedic Rehab, Neurological Rehab, Speech Pathology and Float. I have attached our logo, and some pictures that might be helpful, but the pictures don't have to be included. Here is an example of what I would like it look. http://pixelquarry.com/web-design/contests/brimlotts-website-design-needed-more-work-come-submit-517306/entries/84162975

Health

```html
<!DOCTYPE html>
<html lang="en">
<head>
<meta charset="utf-8">
<title>Verdana Glen Center for Health + Wellness</title>
<link href="https://fonts.googleapis.com/css2?family=Questrial&family=Arimo:wght@400;700&display=swap" rel="stylesheet">
<style>
:root{
  --teal:#86b5a8;
  --teal-dark:#6fa597;
  --green:#a6bd0f;
  --green-light:#bcd10d;
  --green-dark:#7f9409;
  --text:#5f5f5f;
  --text-soft:#555;
  --hero-bg:#d3e5e1;
  --footer-bg:#6b6b6b;
  --footer-text:#e6e6e6;
  --white:#fff;
}
*{box-sizing:border-box;margin:0;padding:0}
html,body{width:1182px;height:1200px;overflow:hidden;background:var(--white)}
body{font-family:"Arimo",Arial,sans-serif;color:var(--text)}
.page{position:relative;width:1182px;height:1200px;overflow:hidden;border-top:4px solid var(--teal)}
.abs{position:absolute}

/* header */
.brand{left:152px;top:48px;display:flex;align-items:center;gap:12px;font-family:"Questrial",sans-serif;font-size:40px;color:var(--teal);letter-spacing:-.5px}
.brand-dot{width:42px;height:42px;border-radius:50%;background:var(--green)}
.social{display:flex;gap:5px}
.social-top{left:730px;top:2px}
.social-icon{width:24px;height:24px;border-radius:50%;border:1.5px solid var(--teal);display:flex;align-items:center;justify-content:center}
.social-footer .social-icon{border:none;background:#c2c2c2}
.account{left:873px;top:-1px;display:flex;gap:6px}
.account a{display:block;height:23px;padding:0 10px;line-height:23px;font-size:12px;color:var(--white);text-decoration:none}
.btn-register{background:var(--teal);width:71px}
.btn-login{background:var(--green);width:74px;text-align:center}
.main-nav{left:652px;top:70px;height:47px;display:flex}
.main-nav a{display:block;height:47px;line-height:54px;padding:0 20px;font-size:13px;color:var(--teal);text-decoration:none;border-left:1px solid #cfdcd8}
.main-nav a:last-child{border-right:1px solid #cfdcd8}
.main-nav a.active{color:var(--green)}

/* hero */
.hero{left:0;top:117px;width:1182px;height:387px;background:radial-gradient(ellipse at 55% 40%,#e4efec 0%,var(--hero-bg) 60%,#c9ddd8 100%);border-top:1px solid var(--teal);border-bottom:1px solid var(--teal)}
.hero-brand{left:152px;top:68px;font-family:"Questrial",sans-serif;font-size:54px;color:var(--teal);letter-spacing:-1px}
.hero-text{left:151px;top:160px;width:440px;font-family:"Questrial",sans-serif;font-size:22px;line-height:27px;color:var(--text)}
.hero-text em{font-style:normal;color:var(--green)}
.btn{display:block;text-align:center;color:var(--white);font-family:"Questrial",sans-serif;text-decoration:none;background:linear-gradient(var(--green-light),#9cb20b);border-bottom:3px solid var(--green-dark);border-radius:3px;text-shadow:0 1px 1px rgba(0,0,0,.25)}
.hero-btn{left:152px;top:262px;width:236px;height:52px;line-height:50px;font-size:21px}
.slider-dots{left:567px;top:367px;display:flex;gap:3px}
.slider-dots span{width:9px;height:9px;border-radius:50%;background:var(--white);border:1px solid #bbb}
.slider-dots span.on{background:var(--green);border-color:var(--green-dark)}

/* services */
.services-title{left:0;top:552px;width:1182px;text-align:center;font-family:"Questrial",sans-serif;font-size:29px;color:var(--text);letter-spacing:.5px}
.services-intro{left:0;top:613px;width:1182px;text-align:center;font-family:"Questrial",sans-serif;font-size:17px;line-height:20px;color:var(--text)}
.service{top:734px;width:210px;text-align:center}
.service-circle{width:152px;height:152px;margin:0 auto;border-radius:50%;border:1px solid var(--teal);display:flex;align-items:center;justify-content:center}
.service-art{width:110px;height:110px;border-radius:50%;background:linear-gradient(135deg,var(--green) 0%,var(--green) 55%,var(--teal) 100%);opacity:.85}
.service h3{margin-top:28px;font-size:17px;font-weight:700;color:var(--text-soft)}
.service p{margin-top:22px;font-size:12.5px;line-height:15px;color:var(--text-soft);padding:0 4px}
.service .btn{margin:24px auto 0;width:193px;height:48px;line-height:46px;font-size:21px}

/* footer */
.site-footer{left:0;top:1123px;width:1182px;height:77px;background:var(--footer-bg);color:var(--footer-text);font-size:11.5px}
.footer-links{left:150px;top:23px}
.footer-links a{color:var(--footer-text);text-decoration:none}
.footer-copy{left:150px;top:43px}
.social-footer{left:885px;top:30px}
</style>
</head>
<body>
<div class="page">

  <header>
    <div class="abs brand"><span class="brand-dot"></span>Verdana Glen</div>

    <div class="abs social social-top">
      <span class="social-icon"></span>
      <span class="social-icon"></span>
      <span class="social-icon"><svg width="12" height="12" viewBox="0 0 12 12"><rect x="3" y="1" width="6" height="3" fill="none" stroke="#86b5a8"/><rect x="1" y="4" width="10" height="4" fill="#86b5a8"/><rect x="3" y="7" width="6" height="4" fill="#fff" stroke="#86b5a8"/></svg></span>
      <span class="social-icon"><svg width="12" height="10" viewBox="0 0 12 10"><rect x="0.5" y="1" width="11" height="8" fill="#86b5a8"/><path d="M1 1.5 6 6 11 1.5" fill="none" stroke="#fff"/></svg></span>
      <span class="social-icon"><svg width="12" height="12" viewBox="0 0 12 12"><path d="M6 1v10M1 6h10" stroke="#86b5a8" stroke-width="2.4"/></svg></span>
    </div>

    <div class="abs account">
      <a class="btn-register" href="#">REGISTER</a>
      <a class="btn-login" href="#">LOGIN</a>
    </div>

    <nav class="abs main-nav">
      <a class="active" href="#">Home</a>
      <a href="#">About us</a>
      <a href="#">Our Sevices</a>
      <a href="#">Contact us</a>
    </nav>
  </header>

  <section class="abs hero">
    <div class="abs hero-brand">Verdana Glen</div>
    <p class="abs hero-text">Donec tortor sapien, pretium pellentesq ue faucibus non, molestie in nulla. Morbi sodales sapien at mi <em>dapibus fringilla.</em></p>
    <a class="abs btn hero-btn" href="#">LEARN MORE</a>
    <div class="abs slider-dots"><span class="on"></span><span></span><span></span><span></span></div>
  </section>

  <h2 class="abs services-title">OUR SERVICES</h2>
  <p class="abs services-intro">Uspendisse potenti. Maecenas egestas neque est, a dapibus lorem convallis et. Phasellus lacinia<br>dui id purus pellentesque suscipit. Aenean adipiscing diam<br>vitae purus hendrerit, a egestas orci lobortis.</p>

  <article class="abs service" style="left:145px">
    <div class="service-circle"><div class="service-art" role="img" aria-label="Knee joint illustration for orthopedic rehab"></div></div>
    <h3>Orthopedic Rehab</h3>
    <p>Nunc facilisis odio leo, id luctus ligula tristique eu. Sed imperdiet erat vitae suscipit interdum.</p>
    <a class="btn" href="#">LEARN MORE</a>
  </article>

  <article class="abs service" style="left:370px">
    <div class="service-circle"><div class="service-art" role="img" aria-label="Head with brain illustration for neurological rehab"></div></div>
    <h3>Neurological Rehab</h3>
    <p>Nunc facilisis odio leo, id luctus ligula tristique eu. Sed imperdiet erat vitae suscipit interdum.</p>
    <a class="btn" href="#">LEARN MORE</a>
  </article>

  <article class="abs service" style="left:599px">
    <div class="service-circle"><div class="service-art" role="img" aria-label="Speaking silhouette illustration for speech pathology"></div></div>
    <h3>Speech Pathology</h3>
    <p>Nunc facilisis odio leo, id luctus ligula tristique eu. Sed imperdiet erat vitae suscipit interdum.</p>
    <a class="btn" href="#">LEARN MORE</a>
  </article>

  <article class="abs service" style="left:824px">
    <div class="service-circle"><div class="service-art" role="img" aria-label="Lotus flower illustration for float therapy"></div></div>
    <h3>Float</h3>
    <p>Nunc facilisis odio leo, id luctus ligula tristique eu. Sed imperdiet erat vitae suscipit interdum.</p>
    <a class="btn" href="#">LEARN MORE</a>
  </article>

  <footer class="abs site-footer">
    <div class="abs footer-links"><a href="#">Home</a> &nbsp;|&nbsp; <a href="#">About us</a> &nbsp;|&nbsp; <a href="#">Our Sevices</a> &nbsp;|&nbsp; <a href="#">Contact us</a></div>
    <div class="abs footer-copy">Copyright © 2014 Verdana Glen Center for Health + Wellness.</div>
    <div class="abs social social-footer">
      <span class="social-icon"></span>
      <span class="social-icon"></span>
      <span class="social-icon"><svg width="12" height="12" viewBox="0 0 12 12"><rect x="3" y="1" width="6" height="3" fill="none" stroke="#fff"/><rect x="1" y="4" width="10" height="4" fill="#fff"/><rect x="3" y="7" width="6" height="4" fill="#c2c2c2" stroke="#fff"/></svg></span>
      <span class="social-icon"><svg width="12" height="10" viewBox="0 0 12 10"><rect x="0.5" y="1" width="11" height="8" fill="#fff"/><path d="M1 1.5 6 6 11 1.5" fill="none" stroke="#c2c2c2"/></svg></span>
      <span class="social-icon"><svg width="12" height="12" viewBox="0 0 12 12"><path d="M6 1v10M1 6h10" stroke="#fff" stroke-width="2.4"/></svg></span>
    </div>
  </footer>

</div>
</body>
</html>
```